20€ Frühlings-Rabatt: Spare jetzt bei Deinem Wettbewerb mit dem Gutscheincode: Mai24
ansprechende Grafik für Leistungserstellungsprozess (Wertstrom) eines Holzbauunternehmens - Infografiken
Zielgruppe
Wir sind ein Holzbauunternehmen mit knapp 100 Mitarbeitern. Unsere Zielgruppen sind öffentliche, gwerbliche und private Bauherren.
Internetseite: lindtal-holzhaus.de
Aufgabenstellung
Der Prozess vom Bauwunsch unserer Kunden bis zur letzten Mängelabnahme soll anschaulich dargestellt werden. Dazu soll aus den bereits vorhandenen, verschiedenen grafischen Darstellungen unseres Leistungserstellungsprozesses (d.h. unseres Wertstromes) eine ansprechende Grafik entwickelt werden. Siehe dazu den Entwurf als Handskizze in elliptischer Form.
Ebenso ist eine Orientierung an unserem Firmenlogo wünschenswert.
Siehe: www.lindtal-holzhaus.de
Die Grafik dient zur Erklärung, Erläuterung unserer wesentlichen Prozess-Schritte für folgende Zielgruppen:
Kunden, Besuchergruppen, vorhandene Mitarbeiter (interne Schulungen), neue Mitarbeiter (Schulungen zur Einarbeitung), für externen Partner (Kommunikation)
Das Grafik soll zur Auflockerung mit passenden, leicht verständlichen, jedoch nicht zu vielen, grafischen Elementen angereichert werden.
Die Grafik soll in einer späteren Ausbaustufe auf eigenen Layern zusätzliche Elemente darstellen (z.B. die Teams, die vorhandenen Softwarewerkzeuge oder die verwendeten Dokumente) darstellen.
Als Grafiksoftware sind CorelDraw und Indesign im Betrieb vorhanden. Vorzugsweise soll die Grafik in diesen Formaten zur Verfügung gestellt werden können.

```html
<!DOCTYPE html>
<html lang="de">
<head>
<meta charset="utf-8">
<title>Lindtal Holzhaus – Wertstrom</title>
<link rel="stylesheet" href="https://fonts.googleapis.com/css2?family=Jost:wght@400;500;600&display=swap">
<style>
  :root {
    --bg: #ffffff;
    --step-top: #b3b3b3;
    --step-bottom: #979797;
    --step-text: #ffffff;
    --green-text: #3a9a22;
    --dot-light: #7ccb4f;
    --dot-dark: #2f9a2a;
    --blue-light: #0a74c9;
    --blue-dark: #0055a3;
    --brand-text: #222222;
  }
  * { margin: 0; padding: 0; box-sizing: border-box; }
  html, body { width: 1200px; height: 787px; overflow: hidden; background: var(--bg); }
  body { position: relative; font-family: "Jost", sans-serif; }

  .brand {
    position: absolute; left: 0; top: 118px; width: 1200px;
    text-align: center; font-weight: 600; font-size: 20px;
    letter-spacing: 0.5px; color: var(--brand-text);
  }

  .step {
    position: absolute; height: 31px;
    background: linear-gradient(var(--step-top), var(--step-bottom));
    color: var(--step-text); font-size: 8.5px; line-height: 1.15;
    display: flex; align-items: center; justify-content: center; text-align: center;
  }
  .step .two { display: flex; flex-direction: column; align-items: center; }
  .step .two span:first-child { border-bottom: 0.6px solid rgba(255,255,255,.7); padding-bottom: 1px; margin-bottom: 2px; }
  .step svg { position: absolute; width: 9px; height: 9px; top: 11px; }
  .step .right { right: 9px; }
  .step .left { left: 9px; }

  .dot {
    position: absolute; width: 17px; height: 17px; border-radius: 50%;
    background: radial-gradient(circle at 40% 35%, var(--dot-light), var(--dot-dark));
  }
  .ok {
    position: absolute; width: 37px; height: 37px; border-radius: 50%;
    background: radial-gradient(circle at 40% 35%, var(--dot-light), var(--dot-dark));
    color: #fff; font-size: 8.5px; text-align: center;
  }
  .ok svg { display: block; margin: 6px auto 0; width: 18px; height: 12px; }
  .ok span { display: block; margin-top: 1px; }

  .label {
    position: absolute; color: var(--green-text); font-size: 8.5px;
    line-height: 1.15; text-align: center; width: 110px;
  }

  .station {
    position: absolute; top: 356px; width: 73px; height: 73px;
    background: linear-gradient(var(--blue-light), var(--blue-dark));
    color: #fff; text-align: center;
  }
  .station svg.icon { display: block; margin: 11px auto 0; }
  .station .name { display: block; font-weight: 500; line-height: 1; }
  .station svg.chev { display: block; margin: 2px auto 0; }
</style>
</head>
<body>
  <div class="brand">LINDTAL HOLZHAUS</div>

  <!-- obere Prozesskette -->
  <div class="step" style="left:87px;top:246px;width:103px;">Marketing
    <svg class="right" viewBox="0 0 10 10"><polyline points="1,1 5,5 1,9" fill="none" stroke="#fff" stroke-width="1"/><polyline points="5,1 9,5 5,9" fill="none" stroke="#fff" stroke-width="1"/></svg></div>
  <div class="dot" style="left:220px;top:253px;"></div>
  <div class="label" style="left:174px;top:281px;">Auftragseingang<br>Architekt</div>

  <div class="step" style="left:268px;top:246px;width:103px;"><div class="two"><span>Planung Architekt</span><span>Beratung</span></div>
    <svg class="right" viewBox="0 0 10 10"><polyline points="1,1 5,5 1,9" fill="none" stroke="#fff" stroke-width="1"/><polyline points="5,1 9,5 5,9" fill="none" stroke="#fff" stroke-width="1"/></svg></div>
  <div class="dot" style="left:401px;top:253px;"></div>
  <div class="label" style="left:355px;top:281px;">Anfrageneingang<br>Bauwerk</div>

  <div class="step" style="left:449px;top:246px;width:118px;">Angebotskalkulation
    <svg class="right" viewBox="0 0 10 10"><polyline points="1,1 5,5 1,9" fill="none" stroke="#fff" stroke-width="1"/><polyline points="5,1 9,5 5,9" fill="none" stroke="#fff" stroke-width="1"/></svg></div>
  <div class="dot" style="left:597px;top:253px;"></div>
  <div class="label" style="left:551px;top:281px;">Angebotsausgang</div>

  <div class="step" style="left:645px;top:246px;width:108px;"><div>Angebots-<br>überarbeitung</div>
    <svg class="right" viewBox="0 0 10 10"><polyline points="1,1 5,5 1,9" fill="none" stroke="#fff" stroke-width="1"/><polyline points="5,1 9,5 5,9" fill="none" stroke="#fff" stroke-width="1"/></svg></div>
  <div class="dot" style="left:783px;top:253px;"></div>
  <div class="label" style="left:737px;top:281px;">Auftragseingang</div>

  <div class="step" style="left:831px;top:246px;width:108px;"><div>Auftragsklärung /<br>- planung</div>
    <svg class="right" viewBox="0 0 10 10"><polyline points="1,1 5,5 1,9" fill="none" stroke="#fff" stroke-width="1"/><polyline points="5,1 9,5 5,9" fill="none" stroke="#fff" stroke-width="1"/></svg></div>
  <div class="dot" style="left:969px;top:253px;"></div>

  <div class="step" style="left:1017px;top:246px;width:95px;"><div>Fertigungs-<br>planung</div>
    <svg class="right" viewBox="0 0 10 10"><polyline points="1,1 5,5 9,1" fill="none" stroke="#fff" stroke-width="1"/><polyline points="1,5 5,9 9,5" fill="none" stroke="#fff" stroke-width="1"/></svg></div>

  <!-- linke Seite -->
  <div class="dot" style="left:114px;top:293px;"></div>
  <div class="label" style="left:68px;top:317px;">Marktrecherche<br>des Kunden</div>

  <div class="station" style="left:87px;">
    <svg class="icon" width="26" height="30" viewBox="0 0 26 30"><circle cx="13" cy="8" r="6" fill="none" stroke="#fff" stroke-width="1.5"/><path d="M2 28 C2 18 24 18 24 28" fill="none" stroke="#fff" stroke-width="1.5"/></svg>
    <span class="name" style="font-size:13px;">Kunde</span>
    <svg class="chev" width="10" height="9" viewBox="0 0 10 10"><polyline points="1,5 5,1 9,5" fill="none" stroke="#fff" stroke-width="1"/><polyline points="1,9 5,5 9,9" fill="none" stroke="#fff" stroke-width="1"/></svg>
  </div>

  <div class="dot" style="left:114px;top:449px;"></div>
  <div class="label" style="left:68px;top:472px;">Abnahme</div>

  <!-- rechte Seite -->
  <div class="ok" style="left:1057px;top:298px;">
    <svg viewBox="0 0 18 12"><polyline points="1,5 7,11 17,1" fill="none" stroke="#fff" stroke-width="1.6"/></svg><span>OK</span></div>

  <div class="station" style="left:1039px;">
    <svg class="icon" width="28" height="28" viewBox="0 0 28 28"><path d="M2 26 V6 H6 V14 L12 9 V14 L18 9 V14 L26 12 V26 Z" fill="none" stroke="#fff" stroke-width="1.4" stroke-linejoin="round"/></svg>
    <span class="name" style="font-size:9.5px;margin-top:3px;">Lieferanten</span>
    <svg class="chev" width="10" height="9" viewBox="0 0 10 10"><polyline points="1,1 5,5 9,1" fill="none" stroke="#fff" stroke-width="1"/><polyline points="1,5 5,9 9,5" fill="none" stroke="#fff" stroke-width="1"/></svg>
  </div>

  <div class="ok" style="left:1057px;top:450px;">
    <svg viewBox="0 0 18 12"><polyline points="1,5 7,11 17,1" fill="none" stroke="#fff" stroke-width="1.6"/></svg><span>OK</span></div>
  <div class="label" style="left:935px;top:463px;text-align:right;">Beschaffungen</div>

  <!-- untere Prozesskette -->
  <div class="step" style="left:87px;top:507px;width:119px;">&nbsp;&nbsp;&nbsp;Fremdleistungen
    <svg class="left" viewBox="0 0 10 10"><polyline points="1,5 5,1 9,5" fill="none" stroke="#fff" stroke-width="1"/><polyline points="1,9 5,5 9,9" fill="none" stroke="#fff" stroke-width="1"/></svg></div>

  <div class="step" style="left:212px;top:507px;width:158px;">Montage
    <svg class="left" viewBox="0 0 10 10"><polyline points="9,1 5,5 9,9" fill="none" stroke="#fff" stroke-width="1"/><polyline points="5,1 1,5 5,9" fill="none" stroke="#fff" stroke-width="1"/></svg></div>

  <div class="ok" style="left:390px;top:504px;">
    <svg viewBox="0 0 18 12"><polyline points="1,5 7,11 17,1" fill="none" stroke="#fff" stroke-width="1.6"/></svg><span>OK</span></div>
  <div class="label" style="left:354px;top:546px;">Montage</div>

  <div class="step" style="left:448px;top:507px;width:51px;">Transport</div>
  <div class="step" style="left:505px;top:507px;width:57px;">Verladung</div>

  <div class="step" style="left:568px;top:507px;width:234px;"><div class="two"><span>Fremdleistungen</span><span>Werkstattproduktion</span></div>
    <svg class="left" viewBox="0 0 10 10"><polyline points="9,1 5,5 9,9" fill="none" stroke="#fff" stroke-width="1"/><polyline points="5,1 1,5 5,9" fill="none" stroke="#fff" stroke-width="1"/></svg></div>

  <div class="ok" style="left:825px;top:504px;">
    <svg viewBox="0 0 18 12"><polyline points="1,5 7,11 17,1" fill="none" stroke="#fff" stroke-width="1.6"/></svg><span>OK</span></div>
  <div class="label" style="left:789px;top:546px;">Werkstatt</div>

  <div class="step" style="left:885px;top:507px;width:227px;">Materiallieferungen
    <svg class="left" viewBox="0 0 10 10"><polyline points="9,1 5,5 9,9" fill="none" stroke="#fff" stroke-width="1"/><polyline points="5,1 1,5 5,9" fill="none" stroke="#fff" stroke-width="1"/></svg></div>
</body>
</html>
```